Business card design needed for rebranded top-end landscaping business

We need a new business card design, incorporating our logo (colours Green #8dc63f and Grey #8a8c8e) and also some options that include the colour dark navy (eg #000040) as our uniforms are navy with white and grey trim.

We are an innovative landscaping company that maintains high-end gardens for meticulous clients. We pride ourselves on our customer service, our professionalism, and our workmanship.

Our business name needs to be easily read and our branding needs to be bold and memorable, without screaming "tradesman"! We prefer clean lines over lots of fine detail.

The design MUST include:
- Business name ("Brambleton Gardenworks")
- Logo (file uploaded)
- Employee name
- Phone number
- Email address
- www.brambletongardenworks.com.au
- Facebook & Instagram logos
- The Turfcraft Guild logo (file uploaded) along with the word "Member"
- Licence "Lic. 618392K"

OPTIONAL inclusions:
- "Creating outdoor spaces for our community to be inspired, refreshed and re-energised"
- "Landscape Maintenance - Irrigation - Arboriculture" (dashes can be replaced with dots or other)
- "Fully qualified, licensed & insured"
- "Residential - Strata - Commercial - Real Estate" (dashes can be replaced with dots or other)

High-end professionals and retirees, real estate agents

Landscaping

See Project description

Sans Serif

Designer to choose colors to be used in the design.

• Must incorporate our logo, and colours Green #8dc63f and Grey #8a8c8e) from the logo, and the colour DARK NAVY (eg #000040).
• The design MUST include:
• - Business name ("Brambleton Gardenworks")
• - Logo (file uploaded)
• - Employee name
• - Phone number
• - Email address
• - www.brambletongardenworks.com.au
• - Facebook & Instagram logos
• - The Turfcraft Guild logo (file uploaded) along with the word "Member"
• - Licence "Lic. 618392K"
• OPTIONAL inclusions:
• - "Creating outdoor spaces for our community to be inspired, refreshed and re-energised"
• - "Landscape Maintenance - Irrigation - Arboriculture" (dashes can be replaced with dots or other)
• - "Fully qualified, licensed & insured"
• - "Residential - Strata - Commercial - Real Estate" (dashes can be replaced with dots or other)

```html
<!DOCTYPE html>
<html lang="en">
<head>
<meta charset="utf-8">
<title>Brambleton Gardenworks – Business Card</title>
<link rel="stylesheet" href="https://fonts.googleapis.com/css2?family=Montserrat:wght@400;500;600;700&display=swap">
<style>
  :root {
    --green: #66b530;
    --grey: #7a7978;
    --text-grey: #6f6f6f;
    --card-fill: #ececec;
    --page: #ffffff;
    --page-edge: #c8c8c8;
  }
  * { margin: 0; padding: 0; box-sizing: border-box; }
  html, body { width: 1010px; height: 1200px; overflow: hidden; background: var(--page); }
  body { font-family: "Montserrat", sans-serif; color: var(--text-grey); }

  .sheet {
    position: relative;
    width: 1010px; height: 1200px;
    border: 1px solid var(--page-edge);
  }
  .card {
    position: absolute;
    left: 72px;
    width: 867px; height: 495px;
  }
  .card--front { top: 61px; }
  .card--back  { top: 617px; }
  .card-frame { position: absolute; inset: 0; width: 100%; height: 100%; }
  .frame-grey { fill: var(--grey); }
  .frame-green { fill: var(--green); }
  .card-face { fill: var(--card-fill); }

  .abs { position: absolute; white-space: nowrap; }

  /* front */
  .brand-mark {
    position: absolute; border-radius: 50%; background: var(--grey);
  }
  .card--front .brand-mark { left: 358px; top: 122px; width: 150px; height: 150px; }
  .brand-name {
    font-weight: 600; color: var(--green); letter-spacing: 0.5px;
  }
  .card--front .brand-name { left: 0; width: 867px; text-align: center; top: 305px; font-size: 44px; }

  .social { position: absolute; top: 428px; display: flex; gap: 8px; left: 755px; }
  .social-dot { width: 34px; height: 34px; border-radius: 50%; }
  .social-dot--one { background: #2f4a86; }
  .social-dot--two { background: #c46a8a; }

  /* back */
  .employee { left: 38px; top: 29px; font-size: 25px; line-height: 35px; }
  .licence { right: 40px; top: 30px; font-size: 21px; }
  .card--back .brand-mark { left: 395px; top: 118px; width: 72px; height: 72px; }
  .card--back .brand-name.small { left: 0; width: 867px; text-align: center; top: 198px; font-size: 20px; }
  .headline {
    left: 104px; width: 657px; top: 248px;
    font-size: 45px; font-weight: 600; color: var(--grey);
    text-align: center; letter-spacing: 0.3px;
  }
  .headline-rule {
    position: absolute; left: 104px; width: 657px; top: 324px;
    height: 2px; background: var(--green);
  }
  .membership { left: 38px; top: 393px; display: flex; align-items: center; gap: 10px; font-size: 18px; }
  .guild-mark { width: 24px; height: 24px; border: 3px solid var(--green); }
  .guild-name { font-size: 17px; letter-spacing: 1.5px; color: var(--text-grey); font-weight: 500; }
  .contact { right: 40px; top: 400px; text-align: right; font-size: 22px; line-height: 30px; }
</style>
</head>
<body>
<div class="sheet">

  <section class="card card--front">
    <svg class="card-frame" viewBox="0 0 1145 654" preserveAspectRatio="none" aria-hidden="true">
      <polygon class="frame-grey" points="0,0 880,0 853,27 26,27 26,627 253,627 226,654 0,654"/>
      <polygon class="frame-green" points="905,0 1145,0 1145,654 277,654 304,627 1118,627 1118,27 878,27"/>
      <rect class="card-face" x="26" y="27" width="1092" height="600"/>
    </svg>
    <div class="brand-mark" aria-hidden="true"></div>
    <div class="abs brand-name">Brambleton Gardenworks</div>
    <div class="social" aria-label="Social media">
      <span class="social-dot social-dot--one"></span>
      <span class="social-dot social-dot--two"></span>
    </div>
  </section>

  <section class="card card--back">
    <svg class="card-frame" viewBox="0 0 1145 654" preserveAspectRatio="none" aria-hidden="true">
      <polygon class="frame-grey" points="0,0 880,0 853,27 26,27 26,627 253,627 226,654 0,654"/>
      <polygon class="frame-green" points="905,0 1145,0 1145,654 277,654 304,627 1118,627 1118,27 878,27"/>
      <rect class="card-face" x="26" y="27" width="1092" height="600"/>
    </svg>
    <div class="abs employee">(Employee Name)<br>(Phone No.)</div>
    <div class="abs licence">Lic. 618392K</div>
    <div class="brand-mark" aria-hidden="true"></div>
    <div class="abs brand-name small">Brambleton Gardenworks</div>
    <div class="abs headline">Brambleton Gardenworks</div>
    <div class="headline-rule"></div>
    <div class="abs membership">
      <span>Member :</span>
      <span class="guild-mark" aria-hidden="true"></span>
      <span class="guild-name">The Turfcraft Guild</span>
    </div>
    <div class="abs contact">(Your Email)@mailbox.com<br>www.brambletongardenworks.com</div>
  </section>

</div>
</body>
</html>
```